a residential painting contractor I need a 6x9 postcard made

I already have a logo, I'm trying to offer my services to people. you can put that there's a 250$ discount for first time customers. include my License number #4627381 as well as the services I offer, interior and exterior painting, pressure washing, cabinet painting, epoxy floors, wood staining, decks, fences and much more. I'm licensed bonded and insured as well.

Target Market(s)

residential consumers (homeowners)

Industry/Entity Type

Painting contractor

Requirements
Must have
• postage stuff on the back I've linked some pictures top right please, my license number, what I do, phone number (555)317-0846 email velbrushworks7@mailzo.net, front and back of postcard
Nice to have
• well lit house in the background, maybe little circles of people doing some of the services I offer

```html
<!DOCTYPE html>
<html lang="en">
<head>
<meta charset="utf-8">
<title>Vel Brushworks – Postcard Front and Back</title>
<link rel="stylesheet" href="https://fonts.googleapis.com/css2?family=Oswald:wght@500;600;700&family=Playfair+Display:wght@700;900&family=Open+Sans:ital,wght@0,400;0,600;0,700;1,700&display=swap">
<style>
  :root {
    --canvas: #e9e7e3;
    --ink: #222226;
    --dark: #2c2c34;
    --mid-gray: #6f6f72;
    --pill-gray: #58585c;
    --panel-light: #f4f4f3;
    --panel-shade: #c9c9c8;
    --white: #ffffff;
    --sky: #a9c3de;
    --wall: #8b8378;
    --lawn: #5f7a45;
    --room: #cfc8bd;
    --siding: #4f5a68;
  }
  * { box-sizing: border-box; margin: 0; padding: 0; }
  html, body { width: 1200px; height: 900px; overflow: hidden; }
  body { background: var(--canvas); font-family: "Open Sans", sans-serif; color: var(--ink); position: relative; }

  .postcard { position: absolute; width: 600px; height: 400px; background: var(--white); overflow: hidden; box-shadow: 0 6px 18px rgba(0,0,0,.18); }
  .postcard--front { left: 60px; top: 40px; }
  .postcard--back { left: 540px; top: 460px; }
  .abs { position: absolute; }

  /* Front */
  .hero-photo { left: 0; top: 0; width: 350px; height: 340px;
    background: linear-gradient(180deg, var(--sky) 0%, #d9e3ec 30%, var(--wall) 55%, #6c6a63 75%, var(--lawn) 100%); }
  .services-panel { left: 340px; top: 0; width: 260px; height: 400px;
    background: linear-gradient(90deg, var(--panel-shade) 0%, var(--panel-light) 45%, var(--panel-light) 100%);
    clip-path: polygon(14px 0, 100% 0, 100% 100%, 0 100%); }
  .headline { right: 18px; top: 12px; text-align: right; font-family: "Playfair Display", serif; font-weight: 900;
    font-size: 23px; line-height: 1.02; color: var(--ink); text-transform: uppercase; }
  .services-pill { left: 355px; top: 78px; width: 245px; height: 26px; background: var(--pill-gray);
    border-radius: 13px 0 0 13px; color: var(--white); font-family: "Oswald", sans-serif; font-weight: 500;
    font-size: 18px; line-height: 26px; text-align: right; padding-right: 22px; }
  .services-list { right: 16px; top: 112px; list-style: none; text-align: right; }
  .services-list li { font-family: "Oswald", sans-serif; font-weight: 500; font-size: 13.5px; line-height: 21.5px;
    text-transform: uppercase; color: var(--ink); display: flex; justify-content: flex-end; align-items: center; gap: 6px; }
  .service-icon { width: 15px; height: 15px; border: 1.5px solid var(--pill-gray); border-radius: 2px; background: var(--white); }
  .license { right: 18px; font-size: 8px; line-height: 1.3; font-weight: 700; color: var(--ink); }
  .front-license { top: 292px; }
  .offer-band { left: 330px; top: 300px; width: 270px; height: 100px; }
  .offer-amount { left: 406px; top: 327px; font-family: "Oswald", sans-serif; font-weight: 700; font-size: 38px; color: var(--white); line-height: 1; }
  .offer-text { left: 500px; top: 331px; font-family: "Oswald", sans-serif; font-weight: 600; font-size: 11.5px; line-height: 1.15; color: var(--white); text-transform: uppercase; }
  .brand-tile { left: 0; top: 82px; width: 80px; height: 86px; background: var(--white); border-radius: 0 10px 10px 0;
    display: flex; flex-direction: column; align-items: center; justify-content: center; gap: 4px; box-shadow: 0 2px 6px rgba(0,0,0,.25); }
  .brand-dot { width: 18px; height: 18px; border-radius: 50%; background: var(--ink); }
  .brand-name { font-family: "Oswald", sans-serif; font-weight: 600; font-size: 12px; line-height: 1.05; text-align: center; color: var(--ink); }
  .thumb { top: 262px; height: 78px; border: 3px solid var(--white); background: linear-gradient(160deg, #e7e2da, var(--room)); }
  .thumb--one { left: 0; width: 95px; }
  .thumb--two { left: 92px; width: 92px; background: linear-gradient(160deg, #dfe3e6, #a9b2b8); }
  .thumb--three { left: 181px; width: 70px; background: linear-gradient(160deg, #bdb4a5, #6f675d); }
  .contact-band { left: 0; top: 340px; width: 340px; height: 60px; }
  .contact-band .band-top { position: absolute; left: 20px; top: 0; width: 320px; height: 40px; background: var(--mid-gray); clip-path: polygon(0 0, 100% 0, 96% 100%, 0 100%); }
  .contact-band .band-bottom { position: absolute; left: 20px; top: 40px; width: 310px; height: 20px; background: #5a5a5d; }
  .front-contact-text { left: 30px; top: 3px; }
  .front-email { left: 34px; top: 43px; }
  .credentials { font-family: "Playfair Display", serif; font-weight: 700; font-size: 13px; line-height: 1.25; color: var(--white); }
  .estimate-row { display: flex; align-items: center; gap: 8px; font-family: "Oswald", sans-serif; font-weight: 600; color: var(--white); line-height: 1.2; }
  .estimate-row .label { font-size: 14px; }
  .estimate-row .phone { font-size: 17px; }
  .phone-icon { width: 12px; height: 14px; }
  .email-row { display: flex; align-items: center; gap: 5px; font-size: 10px; line-height: 1.3; color: var(--white); }
  .email-dot { width: 7px; height: 7px; border-radius: 50%; border: 1.5px solid var(--white); }

  /* Back */
  .mail-side { left: 330px; top: 0; width: 270px; height: 400px; background: var(--white); }
  .before-photo { left: 10px; top: 62px; width: 130px; height: 115px; background: linear-gradient(180deg, #cfdae4 0%, #e7e6e0 45%, #9c9c92 80%, #6d7b55 100%); border: 2px solid var(--white); }
  .after-photo { left: 140px; top: 50px; width: 130px; height: 120px; background: linear-gradient(180deg, #c5d5e3 0%, var(--siding) 45%, #3d4450 75%, #63784b 100%); border: 2px solid var(--white); }
  .photo-tag { width: 46px; height: 14px; background: var(--white); font-family: "Oswald", sans-serif; font-weight: 600; font-size: 9px;
    line-height: 14px; text-align: center; color: var(--ink); transform: rotate(-45deg); }
  .tag-before { left: 2px; top: 72px; }
  .tag-after { left: 132px; top: 60px; }
  .back-panel { left: 0; top: 172px; width: 340px; height: 180px; background: linear-gradient(180deg, var(--panel-shade), var(--panel-light) 40%); }
  .quote-pill { left: 22px; top: 186px; width: 160px; height: 24px; background: var(--pill-gray); border-radius: 12px;
    font-family: "Oswald", sans-serif; font-weight: 500; font-size: 13px; line-height: 24px; color: var(--white); text-align: center; }
  .intro { left: 24px; top: 214px; width: 290px; font-size: 8.5px; line-height: 1.45; color: var(--ink); }
  .intro strong { font-weight: 700; }
  .offer-box { left: 22px; top: 256px; width: 285px; height: 56px; border: 1.5px dashed #8c8c8c; border-radius: 8px; }
  .offer-tab { left: 22px; top: 256px; width: 18px; height: 56px; background: var(--pill-gray); border-radius: 8px 0 0 8px; }
  .offer-tab span { position: absolute; left: 50%; top: 50%; transform: translate(-50%,-50%) rotate(-90deg);
    font-family: "Oswald", sans-serif; font-weight: 600; font-size: 10px; color: var(--white); letter-spacing: 1px; }
  .back-amount { left: 52px; top: 263px; font-family: "Oswald", sans-serif; font-weight: 700; font-size: 38px; line-height: 1; color: var(--ink); }
  .back-offer-text { left: 142px; top: 265px; font-family: "Oswald", sans-serif; font-weight: 600; font-size: 13px; line-height: 1.05; color: var(--ink); text-transform: uppercase; }
  .tagline { left: 40px; top: 315px; font-size: 10px; line-height: 1.3; font-weight: 700; font-style: italic; color: var(--ink); }
  .back-license { left: 160px; right: auto; top: 329px; }
  .back-contact { left: 0; top: 338px; width: 340px; height: 62px; }
  .back-contact-text { left: 22px; top: 346px; }
  .mail-brand { left: 275px; top: 40px; width: 70px; display: flex; flex-direction: column; align-items: center; gap: 3px; }
  .return-address { left: 352px; top: 45px; font-size: 7.5px; line-height: 1.35; color: var(--ink); }
  .return-address .name { font-weight: 700; font-size: 8.5px; }
  .indicia { left: 498px; top: 14px; width: 78px; height: 64px; border: 1px solid var(--ink); font-size: 7.5px; line-height: 1.3; text-align: center; padding-top: 6px; color: var(--ink); }
  .indicia strong { font-weight: 700; }
  .address-box { left: 398px; top: 135px; width: 180px; height: 62px; border: 1px solid var(--ink); background: var(--white); }
  .address-box .route { position: absolute; right: 8px; top: -1px; font-size: 7px; letter-spacing: .5px; background: var(--white); padding: 0 3px; transform: translateY(-50%); }
  .address-box .recipient { position: absolute; left: 14px; top: 24px; font-size: 8.5px; line-height: 1.3; }
</style>
</head>
<body>

<section class="postcard postcard--front" aria-label="Postcard front">
  <div class="abs hero-photo" role="img" aria-label="Well lit two-storey stone and shingle house with a smiling painter in a white apron holding a brush"></div>

  <div class="abs services-panel"></div>
  <h1 class="abs headline">Give your home<br>new life!</h1>
  <div class="abs services-pill">OUR SERVICES:</div>
  <ul class="abs services-list">
    <li>Interior <span class="service-icon"></span></li>
    <li>Exterior painting <span class="service-icon"></span></li>
    <li>Pressure washing <span class="service-icon"></span></li>
    <li>Cabinet painting <span class="service-icon"></span></li>
    <li>Epoxy floors <span class="service-icon"></span></li>
    <li>Wood staining <span class="service-icon"></span></li>
    <li>Decks painting <span class="service-icon"></span></li>
    <li>Fences painting <span class="service-icon"></span></li>
  </ul>
  <p class="abs license front-license">License number #4627381</p>

  <svg class="abs offer-band" viewBox="0 0 270 100" preserveAspectRatio="none" aria-hidden="true">
    <path d="M0 40 Q150 40 270 0 L270 100 L0 100 Z" fill="#2c2c34"/>
  </svg>
  <p class="abs offer-amount">250$</p>
  <p class="abs offer-text">Discount<br>for first time<br>customers</p>

  <div class="abs brand-tile">
    <span class="brand-dot"></span>
    <span class="brand-name">VEL<br>BRUSHWORKS</span>
  </div>

  <div class="abs thumb thumb--one" role="img" aria-label="Bright living room interior"></div>
  <div class="abs thumb thumb--two" role="img" aria-label="Freshly painted lounge with grey floor"></div>
  <div class="abs thumb thumb--three" role="img" aria-label="Stained wooden deck with furniture"></div>

  <div class="abs contact-band">
    <div class="band-top"></div>
    <div class="band-bottom"></div>
    <div class="abs front-contact-text">
      <p class="credentials">Licensed Bonded &amp; Insured</p>
      <div class="estimate-row">
        <span class="label">FREE ESTIMATE!</span>
        <svg class="phone-icon" viewBox="0 0 12 14" aria-hidden="true"><rect x="2" y="0.5" width="8" height="13" rx="1.5" fill="none" stroke="#fff" stroke-width="1.4"/><circle cx="6" cy="11" r="0.9" fill="#fff"/></svg>
        <span class="phone">(555) 317-0846</span>
      </div>
    </div>
    <div class="abs email-row front-email"><span class="email-dot"></span>velbrushworks7@mailzo.net</div>
  </div>
</section>

<section class="postcard postcard--back" aria-label="Postcard back">
  <div class="abs mail-side"></div>

  <div class="abs before-photo" role="img" aria-label="House with worn white siding before painting"></div>
  <div class="abs after-photo" role="img" aria-label="Same house freshly painted dark blue-grey"></div>
  <div class="abs photo-tag tag-before">BEFORE</div>
  <div class="abs photo-tag tag-after">AFTER</div>

  <div class="abs mail-brand">
    <span class="brand-dot"></span>
    <span class="brand-name">VEL<br>BRUSHWORKS</span>
  </div>

  <div class="abs back-panel"></div>
  <div class="abs quote-pill">SCHEDULE A FREE QUOTE</div>
  <p class="abs intro"><strong>VEL BRUSHWORKS</strong> is a professional, efficient and client focused painting company. Our goal is to leave you feeling great and your home looking its best!</p>
  <div class="abs offer-box"></div>
  <div class="abs offer-tab"><span>OFFER</span></div>
  <p class="abs back-amount">250$</p>
  <p class="abs back-offer-text">Discount<br>for first time<br>customers</p>
  <p class="abs tagline">No project is too large or too small.</p>
  <p class="abs license back-license">License number #4627381</p>

  <svg class="abs back-contact" viewBox="0 0 340 62" preserveAspectRatio="none" aria-hidden="true">
    <path d="M0 10 Q170 0 340 4 L330 62 L0 62 Z" fill="#2c2c34"/>
  </svg>
  <div class="abs back-contact-text">
    <p class="credentials">Licensed Bonded &amp; Insured</p>
    <div class="estimate-row">
      <span class="label">FREE ESTIMATE!</span>
      <svg class="phone-icon" viewBox="0 0 12 14" aria-hidden="true"><rect x="2" y="0.5" width="8" height="13" rx="1.5" fill="none" stroke="#fff" stroke-width="1.4"/><circle cx="6" cy="11" r="0.9" fill="#fff"/></svg>
      <span class="phone">(555) 317-0846</span>
    </div>
    <div class="email-row"><span class="email-dot"></span>velbrushworks7@mailzo.net</div>
  </div>

  <div class="abs return-address">
    <p class="name">VEL BRUSHWORKS</p>
    <p>Your Address<br>goes here</p>
  </div>
  <div class="abs indicia">PRSRT STD<br>ECRWSS<br>U.S. Postage<br><strong>PAID</strong><br>EDDM RETAIL</div>
  <div class="abs address-box">
    <span class="route">***********ECRWSS****</span>
    <p class="recipient">Local<br>Postal Customer</p>
  </div>
</section>

</body>
</html>
```